Business Card, Stationary, Fax Cover, and Email Signature
Telvar Capital
Professional
Derek Hollow
President/Founder
418 Bramble Creek Lane, Suite 327
Marlowe, VA 20155
dhollow@telvarcapital.example
www.TelvarCapital.example
Credit Repair - Credit Restoration - Credit Education ( Centered Top)
Legally And Ethically Remove Derogatory Items From Your Credit Report (Bullet Point)
Help Establish New Positive Trade Lines
(Bullet Point)
Learn How To Maintain And Increase Your Credit Score (Bullet Point)
www.TelvarCapital.example (Centered Bottom)

```html
<!DOCTYPE html>
<html lang="en">
<head>
<meta charset="utf-8">
<title>Telvar Capital – Business Card</title>
<link href="https://fonts.googleapis.com/css2?family=Open+Sans:wght@400;600;700&display=swap" rel="stylesheet">
<style>
  :root{
    --backdrop:#6b6e73;
    --card-white:#ffffff;
    --blue-light:#2f72d4;
    --blue-mid:#134aa8;
    --blue-deep:#0a2560;
    --text-light:#ffffff;
    --text-soft:#d5e2f7;
    --brand:#1c4fa3;
    --brand-mark:#2a79d6;
  }
  *{box-sizing:border-box;margin:0;padding:0}
  html,body{width:1200px;height:852px;overflow:hidden}
  body{background:var(--backdrop);font-family:"Open Sans",Arial,sans-serif;position:relative}
  .card{position:absolute;width:520px;height:296px;border-radius:14px;overflow:hidden;display:flex;
        box-shadow:0 8px 22px rgba(0,0,0,.35);background:var(--card-white)}
  .card--first{left:90px;top:140px}
  .card--second{left:590px;top:420px}
  .info-panel{width:58%;height:100%;color:var(--text-light);padding:30px 26px;position:relative;
        background:radial-gradient(ellipse at 30% 40%,var(--blue-light) 0%,var(--blue-mid) 45%,var(--blue-deep) 100%)}
  .card--second .info-panel{text-align:right;
        background:radial-gradient(ellipse at 70% 40%,var(--blue-light) 0%,var(--blue-mid) 45%,var(--blue-deep) 100%)}
  .brand-panel{width:42%;height:100%;display:flex;align-items:center;justify-content:center;gap:10px}
  .brand-mark{width:38px;height:38px;border-radius:50%;background:var(--brand-mark);flex:none}
  .brand-name{font-size:21px;font-weight:600;color:var(--brand);line-height:1.1;white-space:nowrap}
  .person-name{font-size:17px;font-weight:700}
  .person-title{font-size:13px;color:var(--text-soft);margin-bottom:26px}
  .address{font-size:11.5px;line-height:1.45;color:var(--text-soft);margin-bottom:16px}
  .contact-list{list-style:none;font-size:11.5px;line-height:1.55}
  .contact-list li{display:flex;align-items:center;gap:7px;white-space:nowrap}
  .card--second .contact-list li{justify-content:flex-end}
  .contact-list svg{width:11px;height:11px;fill:var(--text-light);flex:none}
</style>
</head>
<body>

<section class="card card--first">
  <div class="info-panel">
    <p class="person-name">Derek Hollow</p>
    <p class="person-title">President/Founder</p>
    <p class="address">418 Bramble Creek Lane<br>Suite 327<br>Marlowe, VA 20155</p>
    <ul class="contact-list">
      <li><svg viewBox="0 0 12 12"><path d="M2 1l2 0 1 3-1.5 1a6 6 0 0 0 3.5 3.5L8 7l3 1v2a1 1 0 0 1-1 1A9 9 0 0 1 1 2a1 1 0 0 1 1-1z"/></svg>(555) 201-4400</li>
      <li><svg viewBox="0 0 12 12"><path d="M2 1l2 0 1 3-1.5 1a6 6 0 0 0 3.5 3.5L8 7l3 1v2a1 1 0 0 1-1 1A9 9 0 0 1 1 2a1 1 0 0 1 1-1z"/></svg>(555) 201-4412</li>
      <li><svg viewBox="0 0 12 12"><rect x="1" y="4" width="10" height="6" rx="1"/><rect x="3" y="1" width="6" height="3"/></svg>(555) 201-4419</li>
      <li><svg viewBox="0 0 12 12"><path d="M1 3h10v6H1z M1 3l5 4 5-4" stroke="#fff" fill="none"/></svg>dhollow@telvarcapital.example</li>
      <li><svg viewBox="0 0 12 12"><circle cx="6" cy="6" r="5"/></svg>www.TelvarCapital.example</li>
    </ul>
  </div>
  <div class="brand-panel">
    <span class="brand-mark"></span>
    <span class="brand-name">Telvar Capital</span>
  </div>
</section>

<section class="card card--second">
  <div class="brand-panel">
    <span class="brand-mark"></span>
    <span class="brand-name">Telvar Capital</span>
  </div>
  <div class="info-panel">
    <p class="person-name">Derek Hollow</p>
    <p class="person-title">President/Founder</p>
    <p class="address">418 Bramble Creek Lane<br>Suite 327<br>Marlowe, VA 20155</p>
    <ul class="contact-list">
      <li>(555) 201-4400<svg viewBox="0 0 12 12"><path d="M2 1l2 0 1 3-1.5 1a6 6 0 0 0 3.5 3.5L8 7l3 1v2a1 1 0 0 1-1 1A9 9 0 0 1 1 2a1 1 0 0 1 1-1z"/></svg></li>
      <li>(555) 201-4412<svg viewBox="0 0 12 12"><path d="M2 1l2 0 1 3-1.5 1a6 6 0 0 0 3.5 3.5L8 7l3 1v2a1 1 0 0 1-1 1A9 9 0 0 1 1 2a1 1 0 0 1 1-1z"/></svg></li>
      <li>(555) 201-4419<svg viewBox="0 0 12 12"><rect x="1" y="4" width="10" height="6" rx="1"/><rect x="3" y="1" width="6" height="3"/></svg></li>
      <li>dhollow@telvarcapital.example<svg viewBox="0 0 12 12"><path d="M1 3h10v6H1z M1 3l5 4 5-4" stroke="#fff" fill="none"/></svg></li>
      <li>www.TelvarCapital.example<svg viewBox="0 0 12 12"><circle cx="6" cy="6" r="5"/></svg></li>
    </ul>
  </div>
</section>

</body>
</html>
```